Fitness industry business card

Dear Designers,

I'm looking to have a business card designed that will appeal to affluent wealthy clients, I would
To have high end clean cut luxurious understated minimalistic feel to the business cards.

I look forward to the first draft of design ideas. I will send the info that I would like to have on the cards shortly.

Best Wishes
Marika

```html
<!DOCTYPE html>
<html lang="en">
<head>
<meta charset="utf-8">
<title>Marika Hale – Personal Trainer Business Card</title>
<link rel="stylesheet" href="https://fonts.googleapis.com/css2?family=Cinzel:wght@700&family=Michroma&family=Open+Sans:wght@400&display=swap">
<style>
  :root {
    --page-bg: #ffffff;
    --card-dark: #232323;
    --card-mid: #2e2e2e;
    --accent-orange: #f07a10;
    --accent-gold: #f7a823;
    --text-light: #f2f2f2;
    --band-text: #1b1b1b;
    --ring-silver: #e9e9e9;
  }
  html, body {
    margin: 0;
    padding: 0;
    width: 1200px;
    height: 900px;
    overflow: hidden;
    background: var(--page-bg);
  }
  .canvas {
    position: relative;
    width: 1200px;
    height: 900px;
  }
  .business-card {
    position: absolute;
    left: 100px;
    top: 150px;
    width: 1000px;
    height: 600px;
    border-radius: 44px;
    background: radial-gradient(ellipse at 40% 35%, var(--card-mid) 0%, var(--card-dark) 70%);
    box-shadow: 0 18px 40px rgba(0,0,0,0.25);
    overflow: hidden;
  }
  .emblem {
    position: absolute;
    left: 55px;
    top: 55px;
    width: 210px;
    height: 210px;
  }
  .trainer-name {
    position: absolute;
    left: 300px;
    top: 78px;
    margin: 0;
    font-family: "Cinzel", serif;
    font-weight: 700;
    font-size: 84px;
    line-height: 1;
    color: var(--accent-gold);
    letter-spacing: 1px;
    white-space: nowrap;
  }
  .trainer-title {
    position: absolute;
    left: 322px;
    top: 188px;
    margin: 0;
    font-family: "Open Sans", sans-serif;
    font-size: 34px;
    letter-spacing: 9px;
    color: var(--text-light);
    white-space: nowrap;
  }
  .specialty-band {
    position: absolute;
    left: 0;
    top: 308px;
    width: 100%;
    height: 24px;
    background: linear-gradient(90deg, var(--accent-orange), var(--accent-gold) 50%, var(--accent-orange));
    display: flex;
    align-items: center;
    gap: 58px;
    padding-left: 60px;
    box-sizing: border-box;
  }
  .specialty {
    font-family: "Michroma", sans-serif;
    font-size: 14px;
    color: var(--band-text);
    font-variant: small-caps;
    letter-spacing: 1px;
    white-space: nowrap;
  }
  .contact-list {
    position: absolute;
    left: 70px;
    top: 420px;
    margin: 0;
    padding: 0;
    list-style: none;
  }
  .contact-item {
    display: flex;
    align-items: center;
    gap: 14px;
    height: 52px;
    font-family: "Open Sans", sans-serif;
    font-size: 32px;
    color: var(--text-light);
  }
  .contact-icon {
    width: 30px;
    height: 30px;
    flex: none;
  }
</style>
</head>
<body>
<div class="canvas">
  <section class="business-card">
    <svg class="emblem" viewBox="0 0 210 210" role="img" aria-label="Emblem: orange silhouette of a running woman inside a silver ring">
      <defs>
        <radialGradient id="emblemFill" cx="50%" cy="50%" r="50%">
          <stop offset="0%" stop-color="#f59a2a"/>
          <stop offset="55%" stop-color="#7a3f10"/>
          <stop offset="100%" stop-color="#1c1c1c"/>
        </radialGradient>
      </defs>
      <circle cx="105" cy="105" r="96" fill="url(#emblemFill)"/>
      <circle cx="105" cy="105" r="96" fill="none" stroke="var(--ring-silver)" stroke-width="7"/>
    </svg>

    <h1 class="trainer-name">Marika Hale</h1>
    <p class="trainer-title">Personal trainer</p>

    <div class="specialty-band">
      <span class="specialty">Pilates instructor</span>
      <span class="specialty">Aqua instructor</span>
      <span class="specialty">Group exercise instructor</span>
    </div>

    <ul class="contact-list">
      <li class="contact-item">
        <svg class="contact-icon" viewBox="0 0 24 24" aria-hidden="true">
          <path fill="var(--accent-orange)" d="M6.6 10.8a15.1 15.1 0 0 0 6.6 6.6l2.2-2.2a1 1 0 0 1 1-.25 11.4 11.4 0 0 0 3.6.57 1 1 0 0 1 1 1V20a1 1 0 0 1-1 1A17 17 0 0 1 3 4a1 1 0 0 1 1-1h3.5a1 1 0 0 1 1 1c0 1.25.2 2.45.57 3.57a1 1 0 0 1-.25 1z"/>
        </svg>
        555-014-2837
      </li>
      <li class="contact-item">
        <svg class="contact-icon" viewBox="0 0 24 24" aria-hidden="true">
          <g fill="none" stroke="var(--accent-orange)" stroke-width="2">
            <circle cx="12" cy="12" r="9.5"/>
            <ellipse cx="12" cy="12" rx="4.2" ry="9.5"/>
            <line x1="2.5" y1="12" x2="21.5" y2="12"/>
            <line x1="4" y1="7" x2="20" y2="7"/>
            <line x1="4" y1="17" x2="20" y2="17"/>
          </g>
        </svg>
        www.fitstridecoach.org
      </li>
      <li class="contact-item">
        <svg class="contact-icon" viewBox="0 0 24 24" aria-hidden="true">
          <rect x="2" y="5" width="20" height="14" rx="1.5" fill="var(--accent-orange)"/>
          <path d="M2.5 6l9.5 7 9.5-7" fill="none" stroke="var(--card-dark)" stroke-width="1.8"/>
        </svg>
        coach@fitstridecoach.org
      </li>
    </ul>
  </section>
</div>
</body>
</html>
```